Boutique custom software development company needs new business card

Our nearly 20 year old custom software development company would like to better include the fact that we are now providing Bitcoin services. These new services are B2B include education (how to acquire and securely hold Bitcoin) and integrating Bitcoin payments into existing ecommerce sites or other existing systems. Please keep the card clean and simple. Attached is our current design and some other files. vexalon.example

Target Market(s)

businesses owners interested in long term relationship

Industry/Entity Type

Custom software development and Bitcoin

Contact Information for Business Card

Marcus Ellwood, marcus@vexalon.example, vexalon.example, (888) 555-VEXAL

Font styles to use
Other font styles liked:
• monospace

Requirements
Must have
• double-sided
Nice to have
• clean and simple
Should not have
• physical address

```html
<!DOCTYPE html>
<html lang="en">
<head>
<meta charset="utf-8">
<title>Vexalon Business Card</title>
<link rel="stylesheet" href="https://fonts.googleapis.com/css2?family=Montserrat:wght@500;700;800&family=Space+Mono:wght@400;700&display=swap">
<style>
  :root {
    --backdrop: #8b8b8b;
    --navy: #0f1942;
    --navy-tile: #16235a;
    --navy-line: #2c3d7e;
    --white: #ffffff;
    --paper: #eef0f3;
    --brand-blue: #2f6fb8;
    --panel-blue: #3b7cc4;
    --panel-blue-light: #5a95d3;
    --accent-orange: #ec7a22;
    --ink: #2b2f38;
    --muted: #6a707c;
    --icon-tone: #8fb6ea;
  }
  * { box-sizing: border-box; margin: 0; padding: 0; }
  html, body { width: 900px; height: 1200px; overflow: hidden; }
  body {
    background: var(--backdrop);
    font-family: "Montserrat", sans-serif;
    position: relative;
  }
  .card {
    position: absolute;
    left: 117px;
    width: 666px;
    height: 366px;
    overflow: hidden;
    box-shadow: 0 4px 14px rgba(0,0,0,0.25);
  }
  /* Front */
  .card-front { top: 264px; background: var(--navy); }
  .front-wordmark {
    position: absolute; top: 86px; left: 0; right: 0;
    text-align: center;
    color: var(--white);
    font-weight: 800;
    font-size: 88px;
    letter-spacing: 2px;
  }
  .services {
    position: absolute; left: 40px; right: 40px; top: 232px;
    display: flex; justify-content: space-between;
  }
  .service {
    width: 132px; height: 90px;
    background: var(--navy-tile);
    border: 1px solid var(--navy-line);
    display: flex; flex-direction: column; align-items: center;
    padding-top: 10px;
  }
  .service-icon {
    width: 34px; height: 34px; border-radius: 8px;
    background: var(--icon-tone);
    margin-bottom: 8px;
  }
  .service-label {
    font-family: "Space Mono", monospace;
    color: var(--white);
    font-size: 10.5px;
    line-height: 1.25;
    text-align: center;
    text-transform: uppercase;
  }
  /* Back */
  .card-back { top: 636px; background: var(--paper); }
  .back-panel { position: absolute; inset: 0; }
  .back-wordmark {
    position: absolute; left: 38px; top: 26px;
    color: var(--brand-blue);
    font-weight: 800;
    font-size: 46px;
    letter-spacing: 1px;
  }
  .tagline {
    position: absolute; left: 40px; top: 82px;
    color: var(--accent-orange);
    font-size: 14px; font-weight: 500;
  }
  .person-name {
    position: absolute; left: 40px; top: 176px;
    color: var(--accent-orange);
    font-size: 27px; font-weight: 700;
    text-transform: uppercase;
  }
  .person-title {
    position: absolute; left: 40px; top: 212px;
    color: var(--muted);
    font-size: 14px; font-weight: 500;
  }
  .contacts {
    position: absolute; left: 40px; top: 246px;
    list-style: none;
    font-family: "Space Mono", monospace;
    font-size: 13.5px;
    color: var(--ink);
  }
  .contacts li { display: flex; align-items: center; height: 28px; }
  .contacts svg { width: 16px; height: 16px; margin-right: 10px; fill: var(--accent-orange); }
</style>
</head>
<body>
  <section class="card card-front">
    <div class="front-wordmark">VEXALON</div>
    <div class="services">
      <div class="service"><div class="service-icon" role="img" aria-label="Application icon"></div><div class="service-label">Web and native<br>applications</div></div>
      <div class="service"><div class="service-icon" role="img" aria-label="Automation icon"></div><div class="service-label">Digital process<br>automation</div></div>
      <div class="service"><div class="service-icon" role="img" aria-label="Cloud portal icon"></div><div class="service-label">Cloud-based<br>portals</div></div>
      <div class="service"><div class="service-icon" role="img" aria-label="Bitcoin consulting icon"></div><div class="service-label">Bitcoin<br>consulting</div></div>
    </div>
  </section>

  <section class="card card-back">
    <svg class="back-panel" viewBox="0 0 666 366" width="666" height="366">
      <polygon points="330,0 666,0 666,366 330,366" fill="var(--panel-blue)"/>
      <polygon points="470,0 590,0 666,90 666,230" fill="var(--panel-blue-light)" opacity="0.55"/>
      <polygon points="330,210 430,366 330,366" fill="var(--accent-orange)"/>
    </svg>
    <div class="back-wordmark">VEXALON</div>
    <div class="tagline">developer of custom applications</div>
    <div class="person-name">Marcus Ellwood</div>
    <div class="person-title">Founder</div>
    <ul class="contacts">
      <li><svg viewBox="0 0 16 16"><path d="M3 1h3l1.5 4-2 1.3a9 9 0 0 0 4.2 4.2L11 8.5l4 1.5v3a2 2 0 0 1-2 2A12 12 0 0 1 1 3a2 2 0 0 1 2-2z"/></svg>(888) 555-VEXAL</li>
      <li><svg viewBox="0 0 16 16"><path d="M1 3h14v10H1z M1 3l7 6 7-6" fill="none" stroke="var(--accent-orange)" stroke-width="1.8"/></svg>marcus@vexalon.example</li>
      <li><svg viewBox="0 0 16 16"><circle cx="8" cy="8" r="6.5" fill="none" stroke="var(--accent-orange)" stroke-width="1.6"/><path d="M1.5 8h13M8 1.5c-3 3.5-3 9.5 0 13M8 1.5c3 3.5 3 9.5 0 13" fill="none" stroke="var(--accent-orange)" stroke-width="1.3"/></svg>www.vexalon.example</li>
    </ul>
  </section>
</body>
</html>
```